Vextor General Painting Ltd. - Construction painting company providing high-quality service

We need a logo and business card design for a painting company that provides high-quality work for major developers and builders in Calgary, Alberta. Our projects include commercial high-rise residential towers. We would like designs that communicate professionalism and high quality service.
Target Market(s)
Developers and builders
Industry/Entity Type
Construction
Contact Information for Business Card
Company name, employee name, title, phone number, email address
Colors
Designer to choose colors to be used in the design.
Look and feel
Each slider illustrates characteristics of the customer's brand and the style your logo design should communicate.

```html
<!DOCTYPE html>
<html lang="en">
<head>
<meta charset="utf-8">
<title>Vextor General Painting Ltd. — Business Card</title>
<link rel="stylesheet" href="https://fonts.googleapis.com/css2?family=Cinzel:wght@400;600&family=Josefin+Sans:wght@400;600&display=swap">
<style>
  :root {
    --bg-light: #f4f4f4;
    --bg-dark: #d9d9d9;
    --ink-grey: #8e8e93;
    --accent-red: #e0522b;
    --accent-orange: #e39a2a;
    --card-white: #f7f7f6;
    --front-left: #dd9022;
    --front-mid: #f2cdb6;
    --front-right: #c0392b;
  }
  * { box-sizing: border-box; margin: 0; padding: 0; }
  html, body { width: 1200px; height: 900px; overflow: hidden; }
  body {
    position: relative;
    background: radial-gradient(ellipse at 50% 40%, var(--bg-light) 0%, var(--bg-dark) 100%);
    font-family: "Josefin Sans", sans-serif;
  }

  .brand-lockup {
    position: absolute;
    left: 44px;
    top: 48px;
    display: flex;
    align-items: center;
    gap: 12px;
  }
  .brand-mark {
    width: 18px;
    height: 18px;
    background: var(--accent-red);
  }
  .brand-name {
    font-family: "Cinzel", serif;
    font-weight: 400;
    font-size: 30px;
    letter-spacing: 1px;
    color: var(--ink-grey);
  }

  .card {
    position: absolute;
    width: 560px;
    height: 320px;
    border-radius: 26px;
    box-shadow: 0 14px 30px rgba(0,0,0,0.18), 0 2px 4px rgba(0,0,0,0.12);
    overflow: hidden;
  }

  .card-front {
    left: 90px;
    top: 150px;
    background: linear-gradient(100deg, var(--front-left) 0%, #e9a63a 30%, var(--front-mid) 55%, #e47752 78%, var(--front-right) 100%);
    display: flex;
    align-items: center;
    justify-content: center;
  }
  .card-front .front-lockup {
    display: flex;
    align-items: center;
    gap: 14px;
  }
  .card-front .front-mark {
    width: 22px;
    height: 22px;
    background: #ffffff;
  }
  .card-front .front-name {
    font-family: "Cinzel", serif;
    font-weight: 400;
    font-size: 26px;
    letter-spacing: 1px;
    color: #ffffff;
  }

  .card-back {
    left: 560px;
    top: 520px;
    background: var(--card-white);
    display: flex;
    align-items: center;
    padding: 0 34px;
  }
  .back-lockup {
    display: flex;
    align-items: center;
    gap: 10px;
    width: 250px;
  }
  .back-mark {
    width: 16px;
    height: 16px;
    background: var(--accent-red);
    flex: none;
  }
  .back-name {
    font-family: "Cinzel", serif;
    font-weight: 400;
    font-size: 16px;
    line-height: 1.3;
    color: var(--ink-grey);
  }
  .divider {
    width: 2px;
    height: 150px;
    margin: 0 26px;
    background: linear-gradient(180deg, var(--accent-orange), var(--accent-red));
    flex: none;
  }
  .contact-block { display: flex; flex-direction: column; gap: 6px; }
  .person-name {
    font-family: "Cinzel", serif;
    font-size: 22px;
    color: var(--ink-grey);
    letter-spacing: 0.5px;
  }
  .job-title {
    font-size: 15px;
    color: var(--accent-red);
    margin-bottom: 10px;
  }
  .contact-line {
    display: flex;
    align-items: center;
    gap: 10px;
    font-size: 14px;
    color: var(--ink-grey);
  }
  .contact-line svg { width: 16px; height: 16px; flex: none; }
</style>
</head>
<body>

  <header class="brand-lockup">
    <span class="brand-mark"></span>
    <span class="brand-name">Vextor General Painting Ltd.</span>
  </header>

  <section class="card card-front" aria-label="Card front">
    <div class="front-lockup">
      <span class="front-mark"></span>
      <span class="front-name">Vextor General Painting Ltd.</span>
    </div>
  </section>

  <section class="card card-back" aria-label="Card back">
    <div class="back-lockup">
      <span class="back-mark"></span>
      <span class="back-name">Vextor General Painting Ltd.</span>
    </div>
    <span class="divider"></span>
    <div class="contact-block">
      <p class="person-name">YOUR NAME</p>
      <p class="job-title">JOB TITLE</p>
      <p class="contact-line">
        <svg viewBox="0 0 24 24" aria-hidden="true"><path fill="#e0522b" d="M6.6 10.8a15.1 15.1 0 0 0 6.6 6.6l2.2-2.2a1 1 0 0 1 1-.25 11.4 11.4 0 0 0 3.6.57 1 1 0 0 1 1 1V20a1 1 0 0 1-1 1A17 17 0 0 1 3 4a1 1 0 0 1 1-1h3.5a1 1 0 0 1 1 1c0 1.25.2 2.45.57 3.57a1 1 0 0 1-.25 1z"/></svg>
        000 000 0000
      </p>
      <p class="contact-line">
        <svg viewBox="0 0 24 24" aria-hidden="true"><rect x="2" y="5" width="20" height="14" rx="1.5" fill="#e0522b"/><path d="M3 6l9 7 9-7" fill="none" stroke="#ffffff" stroke-width="1.6"/></svg>
        youremail@xyz.com
      </p>
    </div>
  </section>

</body>
</html>
```